Qorvant Flyer Design Project

We need a new flyer design for our company based in Australia. We provide Business Valuations for small businesses. The flyer should follow the same colours and theme as our website www.qorvant.com.au and our logo. The design should communicate a professional financial services company. It should be a simple design (not too 'busy') and have a sleek and professional feel to it. It will be used to send to prospective clients and referral sources to tell about our company and prompt them to call us or visit our website.

Target Market(s)

Business owners and people working in financial services (accountants, financial planners etc)

Industry/Entity Type

Financial

Requirements
Must have
• Must be DL double sided, (99mm x 210mm) and use CMYK colours. Must contain trim marks for printer and be print ready.

```html
<!DOCTYPE html>
<html lang="en">
<head>
<meta charset="utf-8">
<title>Qorvant DL Flyer</title>
<link href="https://fonts.googleapis.com/css2?family=Source+Sans+3:ital,wght@0,400;0,600;0,700;1,600&display=swap" rel="stylesheet">
<style>
:root{
  --navy:#1f3a93;
  --blue:#2a9fd8;
  --blue-deep:#1b5fae;
  --sky:#43b6e6;
  --green:#8cc63f;
  --pale:#eef3f8;
  --ink:#000;
  --mark:#9a9a9a;
}
*{margin:0;padding:0;box-sizing:border-box}
html,body{width:1200px;height:674px;overflow:hidden;background:#fff}
body{position:relative;font-family:"Source Sans 3",Arial,sans-serif;color:var(--ink)}
.label{position:absolute;top:8px;font-size:21px;font-weight:700}
.trim{position:absolute;background:var(--mark)}
.trim.v{width:1px;height:33px}
.trim.h{height:1px;width:33px}
.panel{position:absolute;top:65px;width:261px;height:550px;border:1px solid #222;overflow:hidden;background:#fff}
.abs{position:absolute;left:0;width:100%}
.band{position:absolute;left:0;width:100%;height:6px;background:var(--green)}
.brand{position:absolute;left:0;width:100%;text-align:center}
.brand-dot{display:block;margin:0 auto;border-radius:50%;background:var(--blue-deep)}
.brand-name{display:block;font-weight:700;color:var(--navy);line-height:1}
.footer-soft{background:linear-gradient(160deg,#f7fbef 0%,var(--pale) 60%,#ffffff 100%)}
.headline{text-align:center;font-weight:700;line-height:1.05}
.url-tab{position:absolute;background:var(--green);color:var(--navy);font-weight:700;font-size:15px;border-radius:0 0 14px 0;padding-left:24px;line-height:25px}
.tagline{position:absolute;left:0;width:100%;text-align:center;font-style:italic;font-weight:600;font-size:13px;color:var(--navy)}
.tab{position:absolute;left:0;background:var(--green);color:var(--navy);font-weight:700;font-size:15px;line-height:24px;padding-left:15px;border-radius:0 12px 12px 0}
.list{position:absolute;left:15px;right:14px;color:#fff;font-size:9.6px;font-weight:600;list-style:none;line-height:1.2}
.list li{padding-left:6px;text-indent:-6px;margin-bottom:5px}
.list li::before{content:"• "}
.list.tight li{margin-bottom:1.5px}
</style>
</head>
<body>
<div class="label" style="left:89px">Front: Option 1</div>
<div class="label" style="left:514px">Front: Option 2</div>
<div class="label" style="left:935px">Back</div>

<!-- crop marks -->
<div class="trim v" style="left:55px;top:15px"></div><div class="trim v" style="left:316px;top:15px"></div>
<div class="trim v" style="left:472px;top:15px"></div><div class="trim v" style="left:733px;top:15px"></div>
<div class="trim v" style="left:880px;top:15px"></div><div class="trim v" style="left:1141px;top:15px"></div>
<div class="trim v" style="left:55px;top:632px"></div><div class="trim v" style="left:316px;top:632px"></div>
<div class="trim v" style="left:472px;top:632px"></div><div class="trim v" style="left:733px;top:632px"></div>
<div class="trim v" style="left:880px;top:632px"></div><div class="trim v" style="left:1141px;top:632px"></div>
<div class="trim h" style="left:5px;top:65px"></div><div class="trim h" style="left:5px;top:615px"></div>
<div class="trim h" style="left:333px;top:65px"></div><div class="trim h" style="left:333px;top:615px"></div>
<div class="trim h" style="left:422px;top:65px"></div><div class="trim h" style="left:422px;top:615px"></div>
<div class="trim h" style="left:750px;top:65px"></div><div class="trim h" style="left:750px;top:615px"></div>
<div class="trim h" style="left:830px;top:65px"></div><div class="trim h" style="left:830px;top:615px"></div>
<div class="trim h" style="left:1158px;top:65px"></div><div class="trim h" style="left:1158px;top:615px"></div>

<!-- Front option 1 -->
<section class="panel" style="left:55px">
  <div class="brand" style="top:18px">
    <span class="brand-dot" style="width:80px;height:80px"></span>
    <span class="brand-name" style="font-size:32px;margin-top:6px">qorvant</span>
  </div>
  <div class="band" style="top:171px"></div>
  <div class="abs" style="top:177px;height:214px;background:linear-gradient(135deg,#2a8fd8 0%,#1e4fa8 55%,#24267a 100%)" role="img" aria-label="Rising growth chart with a red arrow over a blue grid"></div>
  <div class="band" style="top:391px"></div>
  <div class="abs footer-soft" style="top:397px;height:153px"></div>
  <div class="abs headline" style="top:422px;font-size:21px;color:var(--navy)">Independent<br>Business Valuations</div>
  <div class="url-tab" style="left:-2px;top:472px;width:197px">www.qorvant.com.au</div>
  <div class="tagline" style="top:517px">Small business valuation experts.</div>
</section>

<!-- Front option 2 -->
<section class="panel" style="left:472px">
  <div class="brand" style="top:28px">
    <span class="brand-dot" style="width:126px;height:126px"></span>
    <span class="brand-name" style="font-size:46px;margin-top:10px">qorvant</span>
  </div>
  <div class="band" style="top:230px;height:5px"></div>
  <div class="abs" style="top:235px;height:243px;background:radial-gradient(ellipse at 70% 85%,#8fcdee 0%,#5eb7e6 35%,transparent 36%),linear-gradient(160deg,#4fc0ec 0%,var(--blue) 55%,#2c86cc 100%)"></div>
  <div class="abs headline" style="top:252px;font-size:20px;color:#fff;font-weight:600">Independent<br>Business Valuations</div>
  <div class="url-tab" style="left:-2px;top:425px;width:197px">www.qorvant.com.au</div>
  <div class="band" style="top:478px;height:5px"></div>
  <div class="abs footer-soft" style="top:483px;height:67px"></div>
  <div class="tagline" style="top:517px">Small business valuation experts.</div>
</section>

<!-- Back -->
<section class="panel" style="left:880px">
  <div class="abs" style="top:14px;padding-left:12px">
    <div style="font-size:15px;font-weight:700;color:var(--navy)">Why use Qorvant?</div>
    <div style="font-size:13px;line-height:1.2;margin-top:3px">Before you buy or sell a business,<br>let us check the numbers.</div>
  </div>
  <div class="band" style="top:74px;height:4px"></div>
  <div class="abs" style="top:78px;height:392px;background:radial-gradient(ellipse at 100% 55%,#3c7fcc 0%,transparent 45%),linear-gradient(180deg,var(--sky) 0%,var(--blue) 50%,#2463b4 100%)"></div>
  <div class="tab" style="top:94px;width:196px">How it works:</div>
  <ul class="list" style="top:130px">
    <li>A qualified and experienced Accountant analyses the business.</li>
    <li>Specialised – valuing small businesses</li>
    <li>We use our experience to compare and benchmark similar businesses across Australia</li>
    <li>A valuation appraisal report emailed to you with our comments and valuation estimate.</li>
    <li>A follow up phone call from an accountant to discuss the valuation and answer any questions you have</li>
    <li>Five business day turnaround!</li>
    <li>Fixed price of only $540 (+gst)</li>
  </ul>
  <div class="tab" style="top:318px;width:196px">Our clients include:</div>
  <ul class="list tight" style="top:352px;left:14px">
    <li>Business Buyers and Sellers</li>
    <li>Accountants</li>
    <li>Solicitors</li>
    <li>Financial Planners</li>
    <li>Franchisors and Franchisees</li>
  </ul>
  <div class="abs" style="top:433px;padding-left:15px;color:#fff;font-size:10px;font-weight:600;line-height:1.3">For more information call : 1300 555 214 OR<br>Visit &nbsp;http://www.qorvant.com.au</div>
  <div class="band" style="top:470px;height:5px"></div>
  <div class="abs footer-soft" style="top:475px;height:75px"></div>
  <div style="position:absolute;left:22px;top:478px;width:90px;text-align:center">
    <span class="brand-dot" style="width:42px;height:42px"></span>
    <span class="brand-name" style="font-size:18px;margin-top:3px">qorvant</span>
  </div>
  <div style="position:absolute;left:107px;top:485px;font-size:10px;font-weight:600;color:var(--navy);line-height:1.35">
    Tel: 1300 555 214<br>Fax: 07 5550 1123<br>Email: info@qorvant.com<br>ABN: 41 203 558 917
  </div>
</section>
</body>
</html>
```